Pop up exhibition stand 2000mm (H) x 800mm (W)

I would like a simple pop up banner stand for an exhibition.

We need a pop up banner stand design for 'Brindle Forge Services'

the size is 2000mm(H) x 800mm (W)

Ad copy as follows :

[Brindle Forge logo]

From Sheet Metal To Large Sand Castings

Our Capacity and Rapid Quenching drop bottom ovens deliver precise processing.
We also serve the leading names in aerospace, automotive and advanced engineering.

Visit www.brindleforge-example.co.uk/ or call us Tel: +44 (0)1632 960318

[Put the crafted across the shires logo here, also include the text member somewhere close]

check on their website for other ideas that can help you with this project.

Target Market(s)

will be used at a trade show

Requirements
Nice to have
• modern design for UK manufacturing business

```html
<!DOCTYPE html>
<html lang="en">
<head>
<meta charset="utf-8">
<title>Brindle Forge Services – Exhibition Banner</title>
<link rel="stylesheet" href="https://fonts.googleapis.com/css2?family=Montserrat:wght@600;700&family=Open+Sans:wght@400;600&display=swap">
<style>
  :root {
    --backdrop: #e3e4e6;
    --brand-red: #c8202f;
    --charcoal: #3d3f44;
    --slate: #6b6d73;
    --mist: #d6d7d9;
    --pale: #ecedee;
    --white: #ffffff;
    --steel-dark: #2f3a48;
    --steel-light: #9fb0c2;
  }
  html, body {
    margin: 0;
    padding: 0;
    width: 855px;
    height: 1200px;
    overflow: hidden;
    background: var(--backdrop);
  }
  .banner {
    position: absolute;
    left: 187px;
    top: 0;
    width: 480px;
    height: 1200px;
    overflow: hidden;
    background: var(--white);
    font-family: "Open Sans", Arial, sans-serif;
  }
  .brand {
    position: absolute;
    left: 40px;
    top: 34px;
    display: flex;
    align-items: center;
    gap: 10px;
  }
  .brand-square {
    width: 34px;
    height: 34px;
    background: var(--brand-red);
  }
  .brand-name {
    font-family: "Montserrat", Arial, sans-serif;
    font-weight: 700;
    font-size: 30px;
    color: var(--brand-red);
    line-height: 1;
  }
  .brand-tagline {
    position: absolute;
    left: 84px;
    top: 74px;
    font-size: 12px;
    color: var(--slate);
  }
  .hero-photo {
    position: absolute;
    left: 0;
    top: 118px;
    width: 480px;
    height: 502px;
    background: linear-gradient(100deg, #4a4f57 0%, #8a8e95 35%, #c9cbce 62%, #e6e6e8 100%);
  }
  .shapes {
    position: absolute;
    left: 0;
    top: 0;
  }
  .headline-panel {
    position: absolute;
    left: 0;
    top: 468px;
    width: 340px;
    height: 140px;
    background: rgba(98, 100, 106, 0.9);
    padding: 24px 24px 0 30px;
    box-sizing: border-box;
  }
  .headline {
    margin: 0;
    font-family: "Montserrat", Arial, sans-serif;
    font-weight: 600;
    font-size: 24px;
    line-height: 1.22;
    color: var(--white);
    text-transform: uppercase;
  }
  .headline-rule {
    width: 54px;
    height: 3px;
    background: var(--brand-red);
    margin-top: 12px;
  }
  .body-copy {
    position: absolute;
    left: 70px;
    top: 738px;
    width: 340px;
    text-align: center;
    font-size: 15px;
    line-height: 1.5;
    color: var(--charcoal);
  }
  .body-copy p { margin: 0; }
  .call {
    position: absolute;
    left: 276px;
    top: 942px;
  }
  .call-label {
    font-family: "Montserrat", Arial, sans-serif;
    font-weight: 700;
    font-size: 18px;
    color: var(--brand-red);
    letter-spacing: 1px;
  }
  .call-number {
    font-family: "Montserrat", Arial, sans-serif;
    font-weight: 600;
    font-size: 16px;
    color: var(--charcoal);
  }
  .web-address {
    position: absolute;
    left: 0;
    top: 1112px;
    width: 480px;
    text-align: center;
    font-size: 14px;
    letter-spacing: 1.5px;
    color: var(--white);
  }
</style>
</head>
<body>
<main class="banner">
  <div class="brand">
    <div class="brand-square"></div>
    <div class="brand-name">Brindle Forge</div>
  </div>
  <div class="brand-tagline">specialists in metal heat treatment</div>

  <div class="hero-photo" role="img" aria-label="Photograph of a company representative standing in a heat treatment workshop"></div>

  <svg class="shapes" width="480" height="1200" viewBox="0 0 480 1200">
    <defs>
      <linearGradient id="plant-tones" x1="0" y1="0" x2="1" y2="1">
        <stop offset="0" stop-color="#2f3a48"/>
        <stop offset="0.55" stop-color="#5d6f83"/>
        <stop offset="1" stop-color="#9fb0c2"/>
      </linearGradient>
    </defs>
    <polygon points="0,608 480,608 480,640 240,722 0,640" fill="#ffffff"/>
    <polygon points="0,640 240,722 240,700 0,622" fill="#d6d7d9"/>
    <polygon points="480,640 240,722 240,700 480,622" fill="#ecedee"/>
    <polygon role="img" aria-label="Photograph of a drop bottom quench oven in the plant"
             points="0,880 240,850 480,880 480,932 272,932 222,1020 0,1020" fill="url(#plant-tones)"/>
    <polygon points="0,1020 480,1020 480,1200 0,1200" fill="#6b6d73"/>
    <polygon points="130,1020 350,1020 240,1050" fill="#d6d7d9"/>
  </svg>

  <section class="headline-panel">
    <h1 class="headline">From sheet metal to large sand castings</h1>
    <div class="headline-rule"></div>
  </section>

  <section class="body-copy">
    <p>Our Capacity and Rapid Quenching drop bottom ovens deliver precise processing.</p>
    <p>We also serve the leading names in aerospace, automotive and advanced engineering.</p>
  </section>

  <section class="call">
    <div class="call-label">CALL US</div>
    <div class="call-number">+44 (0)1632 960318</div>
  </section>

  <div class="web-address">www.brindleforge-example.co.uk/</div>
</main>
</body>
</html>
```